family chiropractic health care team needs a modern business card design

Healthcare office with Chiropractors, Physiotherapists, Massage therapists and possibly other practitioners in the future. This is a friendly family office with patients of all ages (and lots of kids) that just moved into a new larger modern office.
Look at the website for photos of the office.
Design for the front and back of a business card required.
Text for the front:
Office logo and name of the office:
Bright Path Wellness Centre
Name of current Practitioner:
Dr. Marten Quovel B.Sc., D.C. Chiropractor
(But please include options to swap out name and title for other practitioners )

address:
218 Farrow Gate
Etobicoke ON.
K2J 6P4
Phone: 416-872-0196 (PATH)
Web site and email:
www.brightpathwellnesscentre.example
brightpathchiro@mailbox.example

2 versions of the back of the card:
1. text below
2. appointment schedule card

Text on back of card:
Chiropractic Card text on back of the card:
There is more to chiropractic than the relief of headaches and back pain! Our primary focus is the integrity of your nerve system, which controls and regulates every cell and tissue of your body. The moving bones of the spinal column can impair this vital communication link between your brain and body. We help improve the function and structure of your spine, reducing nerve system compromise. The result?
Even non-spinal related health problems can show improvement
without drugs
without surgery
regardless of age
for over a century
naturally

Appointment Card info For Back:
Please integrate design elements from the front of the card into an appointment card format.
M Tu W Th F Sat (and a line for writing on beside each one)

```html
<!DOCTYPE html>
<html lang="en">
<head>
<meta charset="utf-8">
<title>Bright Path Wellness Centre – Business Cards</title>
<link rel="stylesheet" href="https://fonts.googleapis.com/css2?family=Open+Sans:wght@400;600&family=Raleway:wght@600;700&family=Montserrat:wght@400&display=swap">
<style>
  :root {
    --stage: #979797;
    --card: #ffffff;
    --green: #8dbb4c;
    --green-soft: #e9f1dc;
    --grey-soft: #e6e6e6;
    --text: #6f6f6f;
    --text-dark: #555555;
    --line: #9a9a9a;
    --band: #222222;
    --band-text: #c9c9c9;
  }
  * { box-sizing: border-box; margin: 0; padding: 0; }
  html, body { width: 1200px; height: 1200px; overflow: hidden; }
  body {
    background: var(--stage);
    font-family: "Open Sans", Arial, sans-serif;
    color: var(--text);
    position: relative;
  }
  .card {
    position: absolute;
    width: 610px;
    height: 356px;
    background: var(--card);
    border-radius: 24px;
    overflow: hidden;
    box-shadow: 0 14px 30px rgba(0,0,0,.28);
  }
  .card--front { left: 295px; top: 39px; }
  .card--info { left: 291px; top: 421px; }
  .card--appointment { left: 291px; top: 809px; }

  .decor {
    position: absolute;
    border-radius: 50% 40% 30% 50%;
    background: radial-gradient(ellipse at 55% 45%, var(--grey-soft) 0%, var(--green-soft) 45%, rgba(255,255,255,0) 72%);
  }
  .card--front .decor { left: 405px; top: 12px; width: 210px; height: 325px; }
  .card--info .decor { left: 440px; top: 0; width: 175px; height: 280px; }

  .brand {
    position: absolute;
    display: flex;
    align-items: center;
    gap: 10px;
    font-family: "Raleway", Arial, sans-serif;
    font-weight: 700;
    color: var(--green);
    line-height: 1.05;
    letter-spacing: .5px;
    text-transform: uppercase;
  }
  .brand__dot { width: 16px; height: 16px; border-radius: 50%; background: var(--green); flex: none; }
  .card--front .brand { left: 150px; top: 40px; font-size: 26px; width: 290px; }
  .card--info .brand { left: 332px; top: 262px; font-size: 23px; width: 260px; }

  .person { position: absolute; right: 322px; top: 178px; text-align: right; font-family: "Raleway", Arial, sans-serif; font-weight: 700; }
  .person__name { color: var(--green); font-size: 21px; }
  .person__title { color: #7c7c7c; font-size: 21px; margin-top: 4px; }
  .divider { position: absolute; width: 1px; background: #bdbdbd; }
  .card--front .divider { left: 306px; top: 168px; height: 78px; }
  .contact { position: absolute; left: 321px; top: 175px; list-style: none; font-size: 14.5px; }
  .contact li { display: flex; align-items: center; gap: 8px; height: 24px; }
  .contact svg { width: 15px; height: 15px; fill: var(--green); flex: none; }
  .address { position: absolute; left: 0; right: 0; top: 315px; text-align: center; font-size: 17px; color: var(--text); }

  .info-left { position: absolute; left: 37px; top: 30px; width: 250px; font-size: 14px; line-height: 20px; }
  .info-left p + p { margin-top: 20px; }
  .card--info .divider { left: 306px; top: 20px; height: 310px; }
  .info-right { position: absolute; left: 331px; top: 30px; width: 255px; font-size: 14px; line-height: 20px; }
  .benefits { list-style: none; margin-top: 20px; }
  .benefits li { display: flex; align-items: center; gap: 3px; }
  .benefits svg { width: 12px; height: 12px; stroke: var(--green); fill: none; stroke-width: 2.4; }

  .schedule { position: absolute; left: 40px; top: 50px; width: 512px; font-family: "Montserrat", Arial, sans-serif; font-size: 17px; color: var(--text); }
  .schedule__row { display: flex; align-items: flex-end; gap: 8px; height: 26px; }
  .schedule__line { flex: 1; border-bottom: 1.5px solid var(--line); height: 14px; margin-right: 10px; }
  .schedule__days { display: flex; justify-content: space-between; margin: 14px 0 38px; }
  .day { display: flex; align-items: center; gap: 4px; }
  .day__box { width: 22px; height: 22px; border: 1.5px solid #999; border-radius: 3px; }
  .band { position: absolute; left: 0; right: 0; bottom: 0; height: 110px; background: var(--band); }
  .band .brand { left: 80px; top: 34px; font-size: 20px; width: 220px; }
  .band__contact { position: absolute; left: 300px; width: 300px; top: 28px; text-align: center; font-size: 14.5px; line-height: 18px; color: var(--band-text); }
  .band__phone { color: var(--green); font-weight: 600; }
</style>
</head>
<body>

<section class="card card--front">
  <div class="decor" role="img" aria-label="Soft faded leaf-and-figure decoration"></div>
  <div class="brand"><span class="brand__dot"></span><span>Bright Path<br>Wellness Centre</span></div>
  <div class="person">
    <div class="person__name">Name Surname</div>
    <div class="person__title">Title</div>
  </div>
  <div class="divider"></div>
  <ul class="contact">
    <li><svg viewBox="0 0 24 24"><path d="M6.6 10.8a15.1 15.1 0 0 0 6.6 6.6l2.2-2.2c.3-.3.7-.4 1-.2 1.1.4 2.3.6 3.6.6.6 0 1 .4 1 1V20c0 .6-.4 1-1 1A17 17 0 0 1 3 4c0-.6.4-1 1-1h3.5c.6 0 1 .4 1 1 0 1.3.2 2.5.6 3.6.1.3 0 .7-.2 1z"/></svg>416-872-0196 (PATH)</li>
    <li><svg viewBox="0 0 24 24"><path d="M2 5h20v14H2z M3 6l9 7 9-7" stroke="#fff" stroke-width="1.5"/></svg>brightpathchiro@mailbox.example</li>
    <li><svg viewBox="0 0 24 24"><circle cx="12" cy="12" r="10"/><path d="M2 12h20M12 2c3 3 3 17 0 20M12 2c-3 3-3 17 0 20" stroke="#fff" stroke-width="1.4" fill="none"/></svg>brightpathwellnesscentre.example</li>
  </ul>
  <p class="address">218 Farrow Gate, Etobicoke, ON K2J 6P4</p>
</section>

<section class="card card--info">
  <div class="decor" role="img" aria-label="Soft faded leaf-and-figure decoration"></div>
  <div class="info-left">
    <p>There is more to chiropractic than the relief of headaches and back pain!</p>
    <p>Our primary focus is the integrity of your nerve system, which controls and regulates every cell and tissue of your body. The moving bones of the spinal column can impair this vital communication link between your brain and body. We help improve the function and structure of your spine, reducing nerve system compromise. The result?</p>
  </div>
  <div class="divider"></div>
  <div class="info-right">
    <p>Even non-spinal related health problems can show improvement</p>
    <ul class="benefits">
      <li><svg viewBox="0 0 12 12"><path d="M1 6l3.5 3.5L11 2"/></svg>without drugs</li>
      <li><svg viewBox="0 0 12 12"><path d="M1 6l3.5 3.5L11 2"/></svg>without surgery</li>
      <li><svg viewBox="0 0 12 12"><path d="M1 6l3.5 3.5L11 2"/></svg>regardless of age</li>
      <li><svg viewBox="0 0 12 12"><path d="M1 6l3.5 3.5L11 2"/></svg>for over a century</li>
      <li><svg viewBox="0 0 12 12"><path d="M1 6l3.5 3.5L11 2"/></svg>naturally</li>
    </ul>
  </div>
  <div class="brand"><span class="brand__dot"></span><span>Bright Path<br>Wellness Centre</span></div>
</section>

<section class="card card--appointment">
  <div class="schedule">
    <div class="schedule__row"><span>Date:</span><span class="schedule__line"></span><span>Time:</span><span class="schedule__line"></span></div>
    <div class="schedule__days">
      <span class="day"><span class="day__box"></span>Mon</span><span class="day"><span class="day__box"></span>Tue</span><span class="day"><span class="day__box"></span>Wed</span><span class="day"><span class="day__box"></span>Thu</span><span class="day"><span class="day__box"></span>Fri</span><span class="day"><span class="day__box"></span>Sat</span><span class="day"><span class="day__box"></span>Sun</span>
    </div>
    <div class="schedule__row"><span>Date:</span><span class="schedule__line"></span><span>Time:</span><span class="schedule__line"></span></div>
    <div class="schedule__days">
      <span class="day"><span class="day__box"></span>Mon</span><span class="day"><span class="day__box"></span>Tue</span><span class="day"><span class="day__box"></span>Wed</span><span class="day"><span class="day__box"></span>Thu</span><span class="day"><span class="day__box"></span>Fri</span><span class="day"><span class="day__box"></span>Sat</span><span class="day"><span class="day__box"></span>Sun</span>
    </div>
  </div>
  <div class="band">
    <div class="brand"><span class="brand__dot"></span><span>Bright Path<br>Wellness Centre</span></div>
    <div class="band__contact">
      <div class="band__phone">416-872-0196 (PATH)</div>
      <div>brightpathchiro@mailbox.example</div>
      <div>brightpathwellnesscentre.example</div>
    </div>
  </div>
</section>

</body>
</html>
```